"Recently Leased" flyer for real estate agency

Looking to have a Recently Leased flyer designed. This will be delivered to apartments and houses closely situated to a property we have recently leased. The idea is to get the attention of owner/landlords in the area that may be considering leasing their property in the future and inform them of the great work we are doing locally. I would like the design to be a two sided flyer using the photoshop (PSD) template below (we would like to be able to edit this once complete should we need to update copy etc in the future). I would like the front page to look like our "for lease sign with the leased sticker on it and copy, I dont want it to look like a typical junk mail flyer.

Target Market(s)

Property owners and investors, male and female aged 28-70

Industry/Entity Type

Real Estate

Font styles to use
Sans Serif

Colors

Designer to choose colors to be used in the design.

Requirements
Must have
• Harbor Keystone Logo
• Contact information
• Copy supplied
Nice to have
• Slick, clean design,
Should not have
• too many colours or too busy a design.
• NO PROPERTY PHOTOS ON FRONT - I want this to be generic and not relate to a specific property image which might confuse people.

```html
<!DOCTYPE html>
<html lang="en">
<head>
<meta charset="utf-8">
<title>Harbor Keystone – Recently Leased Flyer</title>
<link href="https://fonts.googleapis.com/css2?family=Lato:wght@400;700;900&family=Oswald:wght@600&display=swap" rel="stylesheet">
<style>
:root{
  --teal:#1e8a96;
  --teal-light:#2aa3ad;
  --teal-dark:#16707c;
  --ink:#1b1b1b;
  --text:#3a3a3a;
  --sky:#e6eef1;
  --post:#8d9599;
  --paper:#ffffff;
}
*{margin:0;padding:0;box-sizing:border-box}
html,body{width:1200px;height:1200px;overflow:hidden}
body{
  position:relative;
  background:radial-gradient(circle at 50% 45%,#d6d6d6 0%,#a4a4a4 75%);
  font-family:"Lato",sans-serif;color:var(--text);
}
.side-label{
  position:absolute;top:72px;width:424px;text-align:center;
  font-family:"Oswald",sans-serif;font-weight:600;font-size:40px;color:#fff;
}
.side-label.front{left:115px}
.side-label.back{left:649px}
.flyer{
  position:absolute;top:140px;width:424px;height:921px;background:var(--paper);
  box-shadow:0 4px 14px rgba(0,0,0,.35);overflow:hidden;
}
.flyer.front{left:115px}
.flyer.back{left:649px}
.art{position:absolute;left:0;top:0}
.brand{
  position:absolute;font-family:"Lato",sans-serif;font-weight:900;
  font-size:25px;color:var(--ink);white-space:nowrap;
}
.front .brand{top:44px;left:0;width:424px;text-align:center}
.back .brand{top:304px;right:24px}

/* lease sign on the front */
.lease-sign{position:absolute;left:82px;top:112px;width:260px;height:150px;background:var(--paper);
  border:3px solid var(--ink);box-shadow:0 3px 8px rgba(0,0,0,.2)}
.lease-sign .sign-head{height:62px;background:var(--teal);color:#fff;font-weight:900;font-size:34px;
  letter-spacing:2px;text-align:center;line-height:62px}
.lease-sign .sign-name{text-align:center;font-weight:900;font-size:17px;color:var(--ink);margin-top:14px}
.lease-sign .sign-phone{text-align:center;font-weight:700;font-size:15px;color:var(--teal);margin-top:6px}
.leased-sticker{position:absolute;left:170px;top:150px;width:170px;height:44px;background:var(--ink);
  color:#fff;font-weight:900;font-size:28px;letter-spacing:4px;text-align:center;line-height:44px;
  transform:rotate(-14deg);border:3px solid #fff;box-shadow:0 3px 6px rgba(0,0,0,.3)}

.copy{position:absolute;left:24px;right:24px}
.headline{font-weight:700;font-size:17px;color:var(--ink);line-height:26px;text-align:center}
.headline .leased{color:var(--teal)}
.headline .highlight{background:var(--teal);color:#fff;padding:1px 6px}
.intro{font-size:13.4px;line-height:16.5px;margin-top:10px}
.back .intro{font-size:16.2px;font-weight:700;line-height:20px;color:#333}
.benefits{list-style:none;margin-top:10px}
.benefits li{position:relative;padding-left:35px;font-size:13.4px;line-height:16.5px;margin-bottom:10.5px}
.back .benefits li{padding-left:23px;margin-bottom:8px}
.benefits li::before{
  content:"";position:absolute;left:12px;top:3px;width:0;height:0;
  border-left:11px solid var(--teal);border-top:6px solid transparent;border-bottom:6px solid transparent;
}
.back .benefits li::before{left:0}
.closing{font-size:13.4px;line-height:16.5px}
.agent{font-size:17px;font-weight:700;color:var(--teal);margin-top:12px}
.agent-rule{width:115px;height:3px;background:#cfcfcf;margin-top:5px}
.footer{position:absolute;left:0;bottom:0;width:424px;height:92px}
.contact{position:absolute;left:24px;top:14px;font-size:13.6px;color:#fff;line-height:22px}
.contact .row{display:flex;align-items:center;gap:8px}
.contact svg{flex:none}
.contact .gap{margin-left:10px}
</style>
</head>
<body>

<div class="side-label front">Front</div>
<div class="side-label back">Back</div>

<!-- FRONT SIDE -->
<section class="flyer front">
  <svg class="art" width="424" height="400" viewBox="0 0 424 400">
    <defs>
      <linearGradient id="skyFade" x1="0" y1="0" x2="0" y2="1">
        <stop offset="0" stop-color="#ffffff"/>
        <stop offset="1" stop-color="#e2ecef"/>
      </linearGradient>
    </defs>
    <polygon points="0,88 424,88 424,264 230,360 0,280" fill="url(#skyFade)"/>
    <rect x="112" y="262" width="10" height="90" fill="var(--post)"/>
    <rect x="302" y="262" width="10" height="70" fill="var(--post)"/>
    <polygon points="0,280 0,332 240,380" fill="var(--teal)"/>
    <polygon points="0,280 90,310 0,305" fill="var(--teal-dark)"/>
    <polygon points="424,264 424,320 210,372" fill="var(--teal-light)"/>
    <polygon points="424,264 424,290 300,330" fill="var(--teal-dark)"/>
  </svg>
  <div class="brand">HARBOR KEYSTONE</div>

  <div class="lease-sign">
    <div class="sign-head">FOR LEASE</div>
    <div class="sign-name">HARBOR KEYSTONE</div>
    <div class="sign-phone">0400 555 218</div>
  </div>
  <div class="leased-sticker">LEASED</div>

  <div class="copy" style="top:392px">
    <p class="headline">We recently <span class="leased">LEASED</span> a property in your<br>building or street. <span class="highlight">Attracting a great reliable</span><br><span class="highlight">tenant and fantastic return for the owner.</span></p>
    <p class="intro">We received a high number of enquires and applications for this property and have a database of screened and qualified tenants looking to lease in your area.</p>
    <ul class="benefits">
      <li>On average we lease properties 2 weeks faster than the Northern Beaches average</li>
      <li>Strong database of tenants actively looking in the area</li>
      <li>All we do is lease property, no sales – so tenanting and managing your property is our priority</li>
      <li>90 day money back guarantee on our level of service</li>
      <li>Highly competitive, simple all-inclusive pricing.</li>
      <li>Experience the difference of a property management specialist</li>
    </ul>
    <p class="closing">Contact Sam to get your free rental appraisal or transfer your existing investment to an agency that will give it the attention it deserves and maxamise your return.</p>
    <p class="agent">Sam Carver Harbor Keystone</p>
    <div class="agent-rule"></div>
  </div>

  <div class="footer">
    <svg class="art" width="424" height="92" viewBox="0 0 424 92">
      <rect x="0" y="4" width="424" height="88" fill="var(--ink)"/>
      <polygon points="300,92 424,0 424,92" fill="var(--teal-dark)"/>
      <polygon points="340,92 424,30 424,92" fill="var(--teal-light)"/>
    </svg>
    <div class="contact">
      <div class="row">
        <svg width="12" height="12" viewBox="0 0 24 24"><path d="M6 2l4 4-2 3c1 3 4 6 7 7l3-2 4 4-3 4C10 22 2 14 2 5z" fill="var(--teal-light)"/></svg>
        0400 555 218
        <svg class="gap" width="12" height="12" viewBox="0 0 24 24"><circle cx="12" cy="12" r="9" fill="none" stroke="var(--teal-light)" stroke-width="3"/><line x1="3" y1="12" x2="21" y2="12" stroke="var(--teal-light)" stroke-width="2"/></svg>
        www.harborkeystone.example
      </div>
      <div class="row">
        <svg width="12" height="12" viewBox="0 0 24 24"><rect x="2" y="6" width="20" height="14" fill="var(--teal-light)"/><polyline points="2,6 12,14 22,6" fill="none" stroke="var(--ink)" stroke-width="2"/></svg>
        sam@harborkeystone.example
      </div>
      <div class="row">
        <svg width="12" height="12" viewBox="0 0 24 24"><path d="M12 2a7 7 0 0 1 7 7c0 5-7 13-7 13S5 14 5 9a7 7 0 0 1 7-7z" fill="var(--teal-light)"/><circle cx="12" cy="9" r="2.5" fill="var(--ink)"/></svg>
        Level 2, 18 Corran St, Westmere NSW 2199
      </div>
    </div>
  </div>
</section>

<!-- BACK SIDE -->
<section class="flyer back">
  <svg class="art" width="424" height="370" viewBox="0 0 424 370">
    <polygon points="0,0 424,0 424,176 0,340" fill="#a9a59c" role="img" aria-label="Photo of a modern white home with timber deck, pool fencing and palm tree"/>
    <polygon points="0,0 424,0 424,60 0,60" fill="#cfdde6" opacity=".6"/>
    <polygon points="27,0 151,0 330,100" fill="var(--teal)"/>
    <polygon points="319,100 424,60 424,92" fill="var(--teal-light)"/>
    <polygon points="0,340 424,176 424,196 0,362" fill="var(--ink)"/>
    <polygon points="0,362 424,196 424,370 0,370" fill="var(--paper)"/>
  </svg>
  <div class="brand">HARBOR KEYSTONE</div>

  <div class="copy" style="top:380px;left:22px;right:22px">
    <p class="intro" style="margin-top:0">The fundamental idea behind Harbor Keystone Agency was to give landlords a simple and confidence inspiring experience. We achieve this through:</p>
    <ul class="benefits" style="margin-top:12px">
      <li>Unique marketing that goes beyond the standard listing sites and has seen our average days-on-market at 5.9days for 2018.</li>
      <li>A simple, yet competitive fee structure.</li>
      <li>Excellent customer service through an experienced professional property manager.</li>
      <li>Sound advice and communication through out the leasing and management process.</li>
      <li>A simple yet powerful landlord portal which enables owners to view media rich inspection reports, financial reports and maintenance progress at anytime.</li>
      <li>We then back our service promise with a 90day money back guarantee.</li>
    </ul>
    <p class="closing" style="padding-left:4px">Contact Sam to get your free rental appraisal or transfer your existing investment to an agency that will give it the attention it deserves and maxamise your return.</p>
    <p class="agent" style="margin-top:14px">Sam Carver Harbor Keystone</p>
    <div class="agent-rule"></div>
  </div>

  <div class="footer">
    <svg class="art" width="424" height="92" viewBox="0 0 424 92">
      <rect x="0" y="4" width="424" height="88" fill="var(--ink)"/>
      <polygon points="300,92 424,0 424,92" fill="var(--teal-dark)"/>
      <polygon points="340,92 424,30 424,92" fill="var(--teal-light)"/>
    </svg>
    <div class="contact">
      <div class="row">
        <svg width="12" height="12" viewBox="0 0 24 24"><path d="M6 2l4 4-2 3c1 3 4 6 7 7l3-2 4 4-3 4C10 22 2 14 2 5z" fill="var(--teal-light)"/></svg>
        0400 555 218
        <svg class="gap" width="12" height="12" viewBox="0 0 24 24"><circle cx="12" cy="12" r="9" fill="none" stroke="var(--teal-light)" stroke-width="3"/><line x1="3" y1="12" x2="21" y2="12" stroke="var(--teal-light)" stroke-width="2"/></svg>
        www.harborkeystone.example
      </div>
      <div class="row">
        <svg width="12" height="12" viewBox="0 0 24 24"><rect x="2" y="6" width="20" height="14" fill="var(--teal-light)"/><polyline points="2,6 12,14 22,6" fill="none" stroke="var(--ink)" stroke-width="2"/></svg>
        sam@harborkeystone.example
      </div>
      <div class="row">
        <svg width="12" height="12" viewBox="0 0 24 24"><path d="M12 2a7 7 0 0 1 7 7c0 5-7 13-7 13S5 14 5 9a7 7 0 0 1 7-7z" fill="var(--teal-light)"/><circle cx="12" cy="9" r="2.5" fill="var(--ink)"/></svg>
        Level 2, 18 Corran St, Westmere NSW 2199
      </div>
    </div>
  </div>
</section>

</body>
</html>
```